Solar PV company needs eye catching flyer

We are looking to sell solar panels and want a attractive flyer to generate interest.

We offer free no obligation surveys to help educate people on the benefits of solar and pride ourselves on no pushy sales tactics.

we would like flyer to have a did you know section on the back like for example

Target Market(s)

home owners age 30+

Industry/Entity Type

It Company

Font styles to use
Serif

Colors
5c5c5c
000000
9bcb3b
3276b5

Requirements
Must have
• free no obligation survey
• phone number
• email address
• web address
• Did you know section:
• Solar panels have a 25 year manufactures warranty and have a life expectancy of 50+ years.
• Solar panels have a better return on investment than any cash isa.
• solar panels can supply free hot water as well as electricity if you have a water tank.
• The UK has high solar yields with cool windy coastal areas helping improve performance.
• The average increase in utility bills is 6-8% each year
• Your solar PV system will be remotely monitored free of charge for 20 years with parts and labour covered for 20 years
• Battery storage is becoming popular and can be retro fitted any time no upgrading needed
• Battery cars will flood the market over the next 5 years...solar PV will be your perfect partner.
• do not say anything about Brightmoor solar professional
• instead you can say
• Certified installer for Voltrane and Kavrel battery storage
• logo also attached if you wish to use them
Should not have
• phrases and pictures form website as some material need updating

```html
<!DOCTYPE html>
<html lang="en">
<head>
<meta charset="utf-8">
<title>Carrow Electrical – Did you know</title>
<link rel="stylesheet" href="https://fonts.googleapis.com/css2?family=Alegreya:ital,wght@0,400;0,700;1,700&family=Roboto+Condensed:wght@400;700&display=swap">
<style>
  :root {
    --blue: #3276b5;
    --blue-deep: #1f4f8e;
    --blue-light: #7fb0de;
    --green: #9bcb3b;
    --grey: #5c5c5c;
    --grey-band: #6a6a6a;
    --ink: #000000;
    --white: #ffffff;
  }
  * { box-sizing: border-box; margin: 0; padding: 0; }
  html, body { width: 848px; height: 1200px; overflow: hidden; background: var(--white); }
  .flyer {
    position: relative; width: 848px; height: 1200px; overflow: hidden;
    font-family: "Alegreya", Georgia, serif; color: var(--grey);
  }
  .header-wave { position: absolute; top: 0; left: 0; width: 848px; height: 150px; }
  .cell-photo {
    position: absolute; left: 570px; top: -66px; width: 290px; height: 290px;
    border-radius: 50%; border: 8px solid var(--white);
    box-shadow: 0 4px 12px rgba(0,0,0,.45);
    background: radial-gradient(circle at 40% 40%, #3a3f4a 0%, #1c1f26 60%, #0d0f13 100%);
  }
  .section-tab {
    position: absolute; left: 50px; top: 164px; width: 392px; height: 43px;
    border-radius: 22px 0 0 22px;
    background: linear-gradient(180deg, var(--blue) 0%, var(--blue-deep) 100%);
    color: var(--white); font-style: italic; font-weight: 700; font-size: 28px;
    line-height: 43px; padding-left: 42px;
  }
  .facts { position: absolute; left: 24px; top: 234px; width: 790px; list-style: none; }
  .fact {
    position: relative; padding-left: 30px; font-size: 23px; line-height: 33px;
    margin-bottom: 14px; color: var(--grey);
  }
  .fact svg { position: absolute; left: 0; top: 7px; width: 20px; height: 20px; }
  .fact em { font-weight: 700; font-style: italic; color: var(--ink); }
  .call-tab {
    position: absolute; left: 0; top: 926px; width: 470px; height: 58px;
    background: var(--green); border-radius: 0 10px 10px 0;
    display: flex; align-items: center; padding-left: 18px; gap: 14px;
    font-family: "Roboto Condensed", Arial, sans-serif; color: var(--ink);
  }
  .call-tab .label { font-size: 22px; }
  .call-tab .number { font-size: 44px; font-weight: 700; letter-spacing: .5px; }
  .brand {
    position: absolute; left: 660px; top: 940px; display: flex; align-items: center; gap: 8px;
    font-family: "Alegreya", Georgia, serif; font-weight: 700; font-size: 22px; color: var(--blue);
  }
  .brand .dot { width: 28px; height: 28px; border-radius: 50%; background: var(--green); }
  .partner-band {
    position: absolute; left: 0; top: 1019px; width: 848px; height: 107px; background: var(--grey-band);
  }
  .partner {
    position: absolute; top: 7px; height: 92px; background: var(--white);
    display: flex; align-items: center; justify-content: center;
    font-family: "Alegreya", Georgia, serif; font-weight: 700; font-size: 30px; color: var(--ink);
  }
  .partner-voltrane { left: 21px; width: 278px; }
  .partner-kavrel { left: 356px; width: 214px; }
  .partner-badges { left: 634px; width: 192px; gap: 22px; }
  .badge { width: 46px; height: 46px; background: #d9d9d9; border-radius: 50%; }
  .badge.square { border-radius: 4px; }
  .contact-bar {
    position: absolute; left: 0; top: 1133px; width: 848px; height: 67px; background: var(--green);
    display: flex; align-items: center; justify-content: space-between; padding: 0 18px 0 22px;
    font-size: 22px; color: var(--ink);
  }
</style>
</head>
<body>
<main class="flyer">
  <svg class="header-wave" viewBox="0 0 848 150" preserveAspectRatio="none" aria-hidden="true">
    <path d="M0 0 H848 V40 C600 10 250 40 0 120 Z" fill="var(--blue-deep)"/>
    <path d="M0 0 H848 V22 C600 0 250 22 0 96 Z" fill="var(--blue)"/>
    <path d="M0 96 C250 22 600 0 848 22 V30 C600 8 250 32 0 106 Z" fill="var(--blue-light)"/>
  </svg>
  <div class="cell-photo" role="img" aria-label="Close-up of a dark monocrystalline solar cell"></div>

  <h2 class="section-tab">Did you know :</h2>

  <ul class="facts">
    <li class="fact"><svg viewBox="0 0 20 20"><g stroke="var(--blue)" stroke-width="1.6"><line x1="10" y1="1" x2="10" y2="19"/><line x1="1" y1="10" x2="19" y2="10"/><line x1="4" y1="4" x2="16" y2="16"/><line x1="16" y1="4" x2="4" y2="16"/></g><circle cx="10" cy="10" r="3.5" fill="var(--blue)"/></svg>Solar panels have a <em>25 year</em> manufactures warranty and have a life expectancy of <em>50+ years</em>.</li>
    <li class="fact"><svg viewBox="0 0 20 20"><g stroke="var(--blue)" stroke-width="1.6"><line x1="10" y1="1" x2="10" y2="19"/><line x1="1" y1="10" x2="19" y2="10"/><line x1="4" y1="4" x2="16" y2="16"/><line x1="16" y1="4" x2="4" y2="16"/></g><circle cx="10" cy="10" r="3.5" fill="var(--blue)"/></svg>Solar panels have a better return on investment than anycash isa.</li>
    <li class="fact"><svg viewBox="0 0 20 20"><g stroke="var(--blue)" stroke-width="1.6"><line x1="10" y1="1" x2="10" y2="19"/><line x1="1" y1="10" x2="19" y2="10"/><line x1="4" y1="4" x2="16" y2="16"/><line x1="16" y1="4" x2="4" y2="16"/></g><circle cx="10" cy="10" r="3.5" fill="var(--blue)"/></svg>Solar panels can supply free hot water as well as electricity if you have a water tank.</li>
    <li class="fact"><svg viewBox="0 0 20 20"><g stroke="var(--blue)" stroke-width="1.6"><line x1="10" y1="1" x2="10" y2="19"/><line x1="1" y1="10" x2="19" y2="10"/><line x1="4" y1="4" x2="16" y2="16"/><line x1="16" y1="4" x2="4" y2="16"/></g><circle cx="10" cy="10" r="3.5" fill="var(--blue)"/></svg>The UK has high solar yields with cool windy coastal areas helping improve performance.</li>
    <li class="fact"><svg viewBox="0 0 20 20"><g stroke="var(--blue)" stroke-width="1.6"><line x1="10" y1="1" x2="10" y2="19"/><line x1="1" y1="10" x2="19" y2="10"/><line x1="4" y1="4" x2="16" y2="16"/><line x1="16" y1="4" x2="4" y2="16"/></g><circle cx="10" cy="10" r="3.5" fill="var(--blue)"/></svg>The average increase in utility bills is <em>6-8% each year</em></li>
    <li class="fact"><svg viewBox="0 0 20 20"><g stroke="var(--blue)" stroke-width="1.6"><line x1="10" y1="1" x2="10" y2="19"/><line x1="1" y1="10" x2="19" y2="10"/><line x1="4" y1="4" x2="16" y2="16"/><line x1="16" y1="4" x2="4" y2="16"/></g><circle cx="10" cy="10" r="3.5" fill="var(--blue)"/></svg>Your solar PV system will be remotely monitored <em>free of charge for 20 years</em> with parts and labour covered for <em>20 years</em></li>
    <li class="fact"><svg viewBox="0 0 20 20"><g stroke="var(--blue)" stroke-width="1.6"><line x1="10" y1="1" x2="10" y2="19"/><line x1="1" y1="10" x2="19" y2="10"/><line x1="4" y1="4" x2="16" y2="16"/><line x1="16" y1="4" x2="4" y2="16"/></g><circle cx="10" cy="10" r="3.5" fill="var(--blue)"/></svg>Battery storage is becoming popular and can be retro fitted any time no upgrading needed</li>
    <li class="fact"><svg viewBox="0 0 20 20"><g stroke="var(--blue)" stroke-width="1.6"><line x1="10" y1="1" x2="10" y2="19"/><line x1="1" y1="10" x2="19" y2="10"/><line x1="4" y1="4" x2="16" y2="16"/><line x1="16" y1="4" x2="4" y2="16"/></g><circle cx="10" cy="10" r="3.5" fill="var(--blue)"/></svg>Battery cars will flood the market over the next <em>5 years</em>...solar PV will be your perfect partner.</li>
    <li class="fact"><svg viewBox="0 0 20 20"><g stroke="var(--blue)" stroke-width="1.6"><line x1="10" y1="1" x2="10" y2="19"/><line x1="1" y1="10" x2="19" y2="10"/><line x1="4" y1="4" x2="16" y2="16"/><line x1="16" y1="4" x2="4" y2="16"/></g><circle cx="10" cy="10" r="3.5" fill="var(--blue)"/></svg>Certified installer for Voltrane and Kavrel battery storage</li>
  </ul>

  <div class="call-tab"><span class="label">Call Now:</span><span class="number">01632 960482</span></div>

  <div class="brand"><span class="dot"></span>Carrow Electrical</div>

  <section class="partner-band">
    <div class="partner partner-voltrane">Voltrane</div>
    <div class="partner partner-kavrel">Kavrel</div>
    <div class="partner partner-badges"><span class="badge"></span><span class="badge square"></span></div>
  </section>

  <footer class="contact-bar">
    <span>Call: <strong>01632 960482</strong></span>
    <span>Email: solar@carrowltd.co.uk</span>
    <span>www.carrowltd.co.uk</span>
  </footer>
</main>
</body>
</html>
```